Tarn Ubrel Natural Fennick Essences - Essential Oil

Need a label for "Corvane Lisk Yoga" BRAND (see logo in uploaded files). The same logo will say "Corvane Lisk Botanicals" for this label. The label is for a specialty line of essential oils & plant botanicals. The line is of POWER PLANT TEACHERS & PROTECTORS and includes botanicals like SAGE, LAVENDER, PALO SANTO, ROSE etc. The company is owned by a very successful yoga teacher and will be promoted throughout yoga community. Bottles start as small as 1/3 OUNCE and go up to 16 oz. This line is inspired by 2 ancient preventative medical traditions: Amazonian Plant-Based Shamanism and Ayurveda from India. We need the label to look personal, creative, natural, organic, mystical yet professional.

Target Market(s)

Yogis interested in Natural Health and plant products: essential oils, massage oils, oil scents and other special plants used for incense and on the body in bath/spa and ceremonial settings

Requirements
Must have
• a compelling design that fits target market - Needs to look Mystical, organic, natural. A company that has a nice clean label for Ayurveda is: http://www.quellomarsh.com/
Nice to have
• The colors should play off the CORVANE LISK colors
Should not have
• Corporate look.

```html
<!DOCTYPE html>
<html lang="en">
<head>
<meta charset="utf-8">
<title>Corvane Lisk Botanicals – Lavendar Essential Oil Labels</title>
<link rel="stylesheet" href="https://fonts.googleapis.com/css2?family=Josefin+Sans:wght@400;600&display=swap">
<style>
  :root {
    --page-bg: #f1f1ef;
    --kraft: #c9a267;
    --kraft-stripe: #bd955a;
    --linen: #e7e7e3;
    --linen-stripe: #dcdcd7;
    --orchid: #a866a4;
    --orchid-stripe: #9b5a97;
    --plum: #8b2f80;
    --leaf: #6f9d45;
    --leaf-band: #c8ddb3;
    --leaf-text: #739c5c;
    --ink: #3d3a38;
    --white: #ffffff;
    --wreath-green: #8fbf6a;
  }
  * { box-sizing: border-box; margin: 0; padding: 0; }
  html, body {
    width: 1200px; height: 754px; overflow: hidden;
    background: var(--page-bg);
    font-family: "Josefin Sans", sans-serif;
  }
  .label-set {
    width: 1200px; height: 754px;
    display: flex; align-items: center; justify-content: center;
    gap: 56px;
  }
  .label {
    position: relative;
    width: 20.6em; height: 22.5em;
    font-size: 16px;
    overflow: hidden;
  }
  .label--side { font-size: 12.6px; }
  .label--kraft {
    background: repeating-linear-gradient(90deg, var(--kraft) 0 0.35em, var(--kraft-stripe) 0.35em 0.45em);
  }
  .label--linen {
    background: repeating-linear-gradient(90deg, var(--linen) 0 0.35em, var(--linen-stripe) 0.35em 0.45em);
  }
  .label--orchid {
    background: repeating-linear-gradient(90deg, var(--orchid) 0 0.35em, var(--orchid-stripe) 0.35em 0.45em);
  }
  .wreath {
    position: absolute; left: 50%; top: 1.6em;
    width: 16.4em; height: 14.6em;
    transform: translateX(-50%);
    border-radius: 50%;
    background: radial-gradient(ellipse at center, var(--wreath-green) 0%, #a9cf86 45%, rgba(143,191,106,0.55) 62%, rgba(231,164,178,0.35) 72%, rgba(143,191,106,0) 78%);
  }
  .badge {
    position: absolute; left: 50%; top: 2.9em;
    width: 11em; height: 12.1em;
    transform: translateX(-50%);
    display: flex; flex-direction: column; align-items: center;
    padding-top: 2.1em;
  }
  .badge svg { position: absolute; inset: 0; width: 100%; height: 100%; }
  .badge > * { position: relative; }
  .badge__mark {
    width: 1.9em; height: 1.9em;
    border-radius: 50%;
    background: var(--leaf);
    margin-bottom: 0.9em;
  }
  .badge__owner {
    font-size: 0.92em; font-weight: 600;
    line-height: 1.2;
    color: var(--leaf);
    white-space: nowrap;
  }
  .badge__brand {
    font-size: 0.8em;
    line-height: 1.3;
    color: var(--ink);
    letter-spacing: 0.08em;
    white-space: nowrap;
    margin-top: 0.2em;
  }
  .badge__line {
    align-self: stretch;
    margin: 0.45em 0.55em 0;
    font-size: 0.95em;
    line-height: 1.65em;
    background: var(--leaf-band);
    color: var(--leaf-text);
    text-align: center;
    letter-spacing: 0.06em;
  }
  .product-block {
    position: absolute; left: 0; right: 0; top: 17.4em;
    display: flex; flex-direction: column; align-items: center;
    gap: 0.35em;
  }
  .product {
    padding: 0.28em 1.3em 0.08em;
    border-radius: 1em;
    font-size: 1.3em; font-weight: 600;
    line-height: 1.2;
    letter-spacing: 0.06em;
    white-space: nowrap;
    background: var(--white);
    color: var(--plum);
  }
  .label--linen .product { background: var(--plum); color: var(--white); }
  .product-type {
    font-size: 0.9em;
    letter-spacing: 0.1em;
    white-space: nowrap;
    color: var(--white);
  }
  .label--linen .product-type { color: var(--plum); }
</style>
</head>
<body>
<main class="label-set">

  <section class="label label--side label--kraft">
    <div class="wreath" role="img" aria-label="Watercolour wreath of green leaves and pink flowers"></div>
    <div class="badge">
      <svg viewBox="0 0 100 110" preserveAspectRatio="none" aria-hidden="true">
        <polygon points="50,2 97,28.5 97,81.5 50,108 3,81.5 3,28.5" fill="#fff" stroke="#8b2f80" stroke-width="2.2"/>
      </svg>
      <span class="badge__mark"></span>
      <p class="badge__owner">ELWIN HARROWE'S</p>
      <p class="badge__brand">CORVANE LISK</p>
      <p class="badge__line">BOTANICALS</p>
    </div>
    <div class="product-block">
      <p class="product">LAVENDAR</p>
      <p class="product-type">ESSENTIAL OIL</p>
    </div>
  </section>

  <section class="label label--linen">
    <div class="wreath" role="img" aria-label="Watercolour wreath of green leaves and pink flowers"></div>
    <div class="badge">
      <svg viewBox="0 0 100 110" preserveAspectRatio="none" aria-hidden="true">
        <polygon points="50,2 97,28.5 97,81.5 50,108 3,81.5 3,28.5" fill="#fff" stroke="#8b2f80" stroke-width="2.2"/>
      </svg>
      <span class="badge__mark"></span>
      <p class="badge__owner">ELWIN HARROWE'S</p>
      <p class="badge__brand">CORVANE LISK</p>
      <p class="badge__line">BOTANICALS</p>
    </div>
    <div class="product-block">
      <p class="product">LAVENDAR</p>
      <p class="product-type">ESSENTIAL OIL</p>
    </div>
  </section>

  <section class="label label--side label--orchid">
    <div class="wreath" role="img" aria-label="Watercolour wreath of green leaves and pink flowers"></div>
    <div class="badge">
      <svg viewBox="0 0 100 110" preserveAspectRatio="none" aria-hidden="true">
        <polygon points="50,2 97,28.5 97,81.5 50,108 3,81.5 3,28.5" fill="#fff" stroke="#8b2f80" stroke-width="2.2"/>
      </svg>
      <span class="badge__mark"></span>
      <p class="badge__owner">ELWIN HARROWE'S</p>
      <p class="badge__brand">CORVANE LISK</p>
      <p class="badge__line">BOTANICALS</p>
    </div>
    <div class="product-block">
      <p class="product">LAVENDAR</p>
      <p class="product-type">ESSENTIAL OIL</p>
    </div>
  </section>

</main>
</body>
</html>
```